Wordpress Design Project

Need a new website designed for a spin off company we own. We are a On-Site temporary housing Company specializing in rental Mobile homes, Travel trailers, and Park Models. Our clients are homeowners who are looking to do major remodeling jobs on their homes and need to move out of their home for the remodel. We bring in one of our temporary units for them to live in on their site as they remodel. WE also help people who are looking to do new home construction, and want to live on their site as they are building. This Company called " Bright Harbor Homes" is a spin off of our Flagship company called Cobalt Transit Housing (www.cobalthousingco.example) this company rents to people who have a need for on-site housing after a house fire or other disaster. Cobalt rents to Insurance company's who have a insured with a loss ( B2B). Bright Harbor Homes will rent home owners directly ( B2C). We will provide you with photos for a Gallery page, and Videolinks for a video page.

Target Market(s)

people looking to rent a temporary home while they are building a home or remodeling a home

Industry/Entity Type

House

Requirements
Must have
• open - but must have a few photos that I will submit that help tell the story of hat we do.
Nice to have
• links to video we will provide -youtube vids

```html
<!DOCTYPE html>
<html lang="en">
<head>
<meta charset="utf-8">
<title>Bright Harbor Homes</title>
<link rel="stylesheet" href="https://fonts.googleapis.com/css2?family=Questrial&family=Open+Sans:wght@400;600&display=swap">
<style>
:root{
  --page:#ffffff;
  --ink:#222222;
  --text:#333333;
  --brand-red:#d7263d;
  --brand-navy:#1f3f73;
  --rule:#c8c8c8;
  --card:#dcdcdc;
  --card-head:#e3e3e3;
  --btn-top:#4a4a4a;
  --btn-bottom:#111111;
  --accent:#d23a6a;
  --grey-icon:#9a9a9a;
}
*{margin:0;padding:0;box-sizing:border-box}
html,body{width:1200px;height:2462px;overflow:hidden;background:var(--page)}
body{position:relative;font-family:"Open Sans",sans-serif;color:var(--text)}
.abs{position:absolute}

/* header */
.brand{left:16px;top:22px;display:flex;align-items:center;gap:10px}
.brand-mark{width:30px;height:30px;background:var(--brand-red)}
.brand-name{font-family:"Open Sans",sans-serif;font-weight:600;font-size:24px;line-height:1;color:var(--brand-navy);text-transform:uppercase;letter-spacing:.5px;width:190px}
.main-nav{top:50px;left:0;width:1200px;height:20px}
.main-nav a,.foot-nav a{position:absolute;font-family:"Questrial",sans-serif;font-size:14px;color:var(--ink);text-decoration:none;letter-spacing:.6px;white-space:nowrap}

/* hero */
.hero{left:0;top:102px;width:1200px;height:617px;background:linear-gradient(180deg,#6f93c9 0%,#9cb6d8 25%,#b9bcb8 45%,#9ea39d 62%,#5f8a3c 82%,#4f7a2e 100%)}
.hero-arrow{position:absolute;top:166px;width:66px;height:123px;background:var(--accent);display:flex;align-items:center;justify-content:center}
.hero-arrow.prev{left:0}
.hero-arrow.next{right:0}
.hero-caption{position:absolute;left:92px;top:456px;width:967px;height:151px;background:rgba(235,238,235,.82);text-align:center;font-family:"Questrial",sans-serif;font-size:34px;letter-spacing:2px;color:#3a3a3a;line-height:53px;padding-top:22px;text-transform:uppercase}

/* thumbnail strip */
.strip{left:0;top:719px;width:1200px;height:192px;background:#fff;box-shadow:0 10px 14px -6px rgba(0,0,0,.25)}
.thumb{position:absolute;top:18px;width:227px;height:159px}
.strip-arrow{position:absolute;top:76px;width:42px;height:42px;border-radius:50%;border:2px solid #c9c9c9;background:#f2f2f2;display:flex;align-items:center;justify-content:center}

/* sections */
.section-title{font-family:"Open Sans",sans-serif;font-size:21px;color:var(--ink);text-transform:uppercase;padding-bottom:2px;border-bottom:1px solid var(--rule);line-height:26px}
.copy{font-size:13px;line-height:21.5px;color:var(--text);letter-spacing:.3px;width:1146px}
.copy p+p{margin-top:23px}
.read-more{display:flex;align-items:center;justify-content:space-between;width:109px;height:29px;padding:0 8px 0 10px;border-radius:3px;background:linear-gradient(180deg,var(--btn-top),var(--btn-bottom));color:#fff;font-size:10px;font-weight:600;letter-spacing:.3px;text-decoration:none;box-shadow:1px 1px 2px rgba(0,0,0,.35)}
.divider{left:26px;width:1146px;height:1px;background:var(--rule)}

/* cards */
.card{position:absolute;background:var(--card)}
.card-title{background:var(--card-head);height:54px;padding-left:12px;font-size:21px;line-height:54px;color:var(--ink);text-transform:uppercase}
.card-media{position:relative;height:214px;display:flex;align-items:center;justify-content:center}
.card .read-more{position:absolute;left:17px;bottom:23px}
.play{width:44px;height:44px;border-radius:50%;border:3px solid #fff;background:rgba(40,40,40,.55);display:flex;align-items:center;justify-content:center}

/* footer */
.foot-rule{left:26px;width:1146px;height:1px;background:var(--rule)}
.foot-brand{left:30px;top:2354px;display:flex;align-items:center;gap:8px}
.foot-brand-mark{width:22px;height:22px;background:var(--brand-red)}
.foot-brand-name{font-size:20px;font-weight:600;color:#333;text-transform:uppercase;line-height:1}
.copyright{left:28px;top:2420px;font-size:12px;color:#333;letter-spacing:.4px}
.social{left:916px;top:2377px;display:flex;gap:14px}
.social span{width:27px;height:27px;border-radius:50%;background:var(--grey-icon)}
.social span:first-child{background:#2a2a2a}
</style>
</head>
<body>

<header>
  <div class="abs brand">
    <span class="brand-mark"></span>
    <span class="brand-name">Bright Harbor Homes</span>
  </div>
  <nav class="abs main-nav">
    <a style="left:381px">HOME</a>
    <a style="left:468px">SERVICES</a>
    <a style="left:581px">FLOOR PLANS</a>
    <a style="left:726px">GALLERY</a>
    <a style="left:829px">VIDEOS</a>
    <a style="left:927px">TESTIMONIALS</a>
    <a style="left:1074px">CONTACT US</a>
  </nav>
</header>

<section class="abs hero" role="img" aria-label="Photo of a single-wide mobile home with grey siding set up on a grassy lot under a blue sky">
  <span class="hero-arrow prev"><svg width="24" height="30" viewBox="0 0 24 30"><path d="M18 3 L6 15 L18 27" fill="none" stroke="#fff" stroke-width="5"/></svg></span>
  <span class="hero-arrow next"><svg width="24" height="30" viewBox="0 0 24 30"><path d="M6 3 L18 15 L6 27" fill="none" stroke="#fff" stroke-width="5"/></svg></span>
  <div class="hero-caption">Welcome to Cobalt Housing<br>Your Onsite Temporary Housing Experts</div>
</section>

<section class="abs strip">
  <span class="strip-arrow" style="left:28px"><svg width="14" height="16" viewBox="0 0 14 16"><path d="M11 1 L3 8 L11 15 Z" fill="#c4c4c4"/></svg></span>
  <div class="thumb" style="left:84px;background:linear-gradient(180deg,#8fb0d8,#d9cdb4 45%,#cfc3a8 75%,#7d7d7d)" role="img" aria-label="Photo of a beige mobile home with dark shutters"></div>
  <div class="thumb" style="left:351px;background:linear-gradient(180deg,#7ea5d6,#e4d7b8 40%,#f2e7cf 70%,#6e8f48)" role="img" aria-label="Photo of a park model cabin with a white front porch"></div>
  <div class="thumb" style="left:619px;background:linear-gradient(180deg,#86abd9,#eef0f2 40%,#d9dcdf 70%,#567f35)" role="img" aria-label="Photo of white travel trailers parked in a row"></div>
  <div class="thumb" style="left:886px;background:linear-gradient(180deg,#a8b1a0,#f0f0f0 45%,#d8d8d8 75%,#8a8a8a)" role="img" aria-label="Photo of a white mobile home set up on a residential lot"></div>
  <span class="strip-arrow" style="left:1128px"><svg width="14" height="16" viewBox="0 0 14 16"><path d="M3 1 L11 8 L3 15 Z" fill="#c4c4c4"/></svg></span>
</section>

<section class="about">
  <h2 class="abs section-title" style="left:30px;top:961px">About Us</h2>
  <div class="abs copy" style="left:28px;top:1015px">
    <p>We are the leading provider of On-Site Temporary Housing.&nbsp; We provide Mobile Homes, Park Models and Travel Trailers. These homes are brought to your client's home site and set up. Your client can stay right at home to oversee the reconstruction.</p>
    <p>We have been in the On-Site Temporary Housing business for over 30 years. We have a courteous and experienced staff.</p>
  </div>
  <a class="abs read-more" style="left:26px;top:1128px">READ MORE <svg width="14" height="10" viewBox="0 0 14 10"><path d="M1 1 L5 5 L1 9 M7 1 L11 5 L7 9" fill="none" stroke="#fff" stroke-width="1.6"/></svg></a>
</section>

<div class="abs divider" style="top:1182px"></div>

<section class="how">
  <h2 class="abs section-title" style="left:26px;top:1194px">How It Works</h2>
  <div class="abs copy" style="left:28px;top:1250px">
    <p>We provide the best On-Site Homes in the nation. Our service is second to none. We have a experienced and friendly staff. We are simply the BEST On-Site housing company you will ever work with.</p>
  </div>
  <a class="abs read-more" style="left:26px;top:1320px">READ MORE <svg width="14" height="10" viewBox="0 0 14 10"><path d="M1 1 L5 5 L1 9 M7 1 L11 5 L7 9" fill="none" stroke="#fff" stroke-width="1.6"/></svg></a>
</section>

<div class="abs divider" style="top:1371px"></div>

<section class="products">
  <h2 class="abs section-title" style="left:28px;top:1391px">Products</h2>
  <article class="card" style="left:25px;top:1438px;width:361px;height:345px">
    <h3 class="card-title">Mobile Homes</h3>
    <div class="card-media" style="background:linear-gradient(160deg,#c9b89a,#8b7a5a 50%,#a35a2c)" role="img" aria-label="Photo of a furnished mobile home living room"></div>
    <a class="read-more">READ MORE <svg width="14" height="10" viewBox="0 0 14 10"><path d="M1 1 L5 5 L1 9 M7 1 L11 5 L7 9" fill="none" stroke="#fff" stroke-width="1.6"/></svg></a>
  </article>
  <article class="card" style="left:419px;top:1438px;width:359px;height:345px">
    <h3 class="card-title">Park Models</h3>
    <div class="card-media" style="background:linear-gradient(180deg,#e9ecef,#3f5a2c 40%,#c9bfa6 60%,#8e8e8e)" role="img" aria-label="Photo of a row of park model homes on a gravel lot"></div>
    <a class="read-more">READ MORE <svg width="14" height="10" viewBox="0 0 14 10"><path d="M1 1 L5 5 L1 9 M7 1 L11 5 L7 9" fill="none" stroke="#fff" stroke-width="1.6"/></svg></a>
  </article>
  <article class="card" style="left:811px;top:1438px;width:361px;height:345px">
    <h3 class="card-title">Travel Trailers</h3>
    <div class="card-media" style="background:linear-gradient(180deg,#8cb2e0,#f2f3f5 35%,#dcdfe2 70%,#6d8f44)" role="img" aria-label="Photo of a white travel trailer parked on a driveway"></div>
    <a class="read-more">READ MORE <svg width="14" height="10" viewBox="0 0 14 10"><path d="M1 1 L5 5 L1 9 M7 1 L11 5 L7 9" fill="none" stroke="#fff" stroke-width="1.6"/></svg></a>
  </article>
</section>

<section class="videos">
  <h2 class="abs section-title" style="left:28px;top:1814px">Video Gallery</h2>
  <article class="card" style="left:25px;top:1865px;width:361px;height:345px">
    <h3 class="card-title">Elite Travel Trailer</h3>
    <div class="card-media" style="background:linear-gradient(150deg,#d9b27a,#a2723e 50%,#3a2a1e)" role="img" aria-label="Video still of a travel trailer kitchen with pine cabinets">
      <span class="play"><svg width="16" height="18" viewBox="0 0 16 18"><path d="M3 1 L15 9 L3 17 Z" fill="#fff"/></svg></span>
    </div>
    <a class="read-more">READ MORE <svg width="14" height="10" viewBox="0 0 14 10"><path d="M1 1 L5 5 L1 9 M7 1 L11 5 L7 9" fill="none" stroke="#fff" stroke-width="1.6"/></svg></a>
  </article>
  <article class="card" style="left:419px;top:1865px;width:359px;height:345px">
    <h3 class="card-title">Standard Mobile Home</h3>
    <div class="card-media" style="background:linear-gradient(180deg,#86abd9,#eef0f2 40%,#d9dcdf 70%,#567f35)" role="img" aria-label="Video still of white travel trailers parked in a row">
      <span class="play"><svg width="16" height="18" viewBox="0 0 16 18"><path d="M3 1 L15 9 L3 17 Z" fill="#fff"/></svg></span>
    </div>
    <a class="read-more">READ MORE <svg width="14" height="10" viewBox="0 0 14 10"><path d="M1 1 L5 5 L1 9 M7 1 L11 5 L7 9" fill="none" stroke="#fff" stroke-width="1.6"/></svg></a>
  </article>
  <article class="card" style="left:811px;top:1865px;width:361px;height:345px">
    <h3 class="card-title">Mobile Home Set Up</h3>
    <div class="card-media" style="background:linear-gradient(180deg,#f4f4f4,#e2d6bd 40%,#d3c6a9 80%,#bdb4a0)" role="img" aria-label="Video still of a beige mobile home with dark shutters">
      <span class="play"><svg width="16" height="18" viewBox="0 0 16 18"><path d="M3 1 L15 9 L3 17 Z" fill="#fff"/></svg></span>
    </div>
    <a class="read-more">READ MORE <svg width="14" height="10" viewBox="0 0 14 10"><path d="M1 1 L5 5 L1 9 M7 1 L11 5 L7 9" fill="none" stroke="#fff" stroke-width="1.6"/></svg></a>
  </article>
</section>

<footer>
  <div class="abs foot-rule" style="top:2280px"></div>
  <nav class="abs foot-nav" style="left:0;top:2291px;width:1200px;height:20px">
    <a style="left:204px">HOME</a>
    <a style="left:291px">SERVICES</a>
    <a style="left:404px">FLOOR PLANS</a>
    <a style="left:547px">GALLERY</a>
    <a style="left:652px">VIDEOS</a>
    <a style="left:750px">TESTIMONIALS</a>
    <a style="left:896px">CONTACT US</a>
  </nav>
  <div class="abs foot-rule" style="top:2321px"></div>
  <div class="abs foot-brand">
    <span class="foot-brand-mark"></span>
    <span class="foot-brand-name">Cobalt Housing</span>
  </div>
  <p class="abs copyright">COBALT HOUSING © 2013 | ALL RIGHTS RESERVED</p>
  <div class="abs social" aria-label="Social links">
    <span></span><span></span><span></span><span></span><span></span><span></span>
  </div>
</footer>

</body>
</html>
```